Web Design Project

The Varnholt Group is a strategy consulting group that works primarily with the healthcare industry. We provide a limited range of strategic planning & marketing services designed to focus on the growth and future viability of our clients’ organizations. We are a very small organization, but want to communicate a sense of boldness, forward-looking/visionary, and both creative and analytic. What follows below is: 1) A simple overview of the outline of the web-pages; 2) an important list of web-sites that appeal to me – the most important of which appears in a larger font; 3) photo ideas for the home page (from Pictavo.com). I have not written copy…and won’t until I know length based upon design.

The Varnholt Group
Healthcare Strategic Consulting

(Key Sections for the site)
HOME PAGE ABOUT US SERVICES NEWS & COMMENTS CONTACT US

(Sites That I Admire:)

http://www.lumenwirk.eu/services/ Very creative use of iconography to represent services, etc.

http://quillmoss.com/ Arresting graphics

http://brontiva.co/ GREAT SITE. THIS IS THE SITE THAT I LIKE THE MOST IN TERMS OF GENERAL LOOK & FEEL.

http://kasperholm.com/ Very interesting, stark/bold B&W site for architects

http://www.rtmalvey.com/ Interesting home page for promoting individual

HOME PAGE:

The Varnholt Group
STRATEGIC CONSULTING SERVICES (should be bold). We have a Logo that can be supplied later

Pictavo Image Options: 47193652, 36840157, 29617483, 58302619, 274815936, 61948237
Updates

Project Deadline Extended
Reason: The 1st and 2nd place designers will have an additional 5-7 days to complete the remaining pages of the site (approximately 11 pages). I have a file with all the photo information and rough copy that can be dropped into position.

Target Market(s)

Senior Executives (CEO,COO, CFO,SVP) in major hospitals or healthcare systems, other senior executives within healthcare.

Industry/Entity Type

Healthcare

Requirements
Must have
• I will want to pay to have this project expanded to show look and feel for:
*Home Page and key sections
*4 Pages that will be under the "About Us" heading
*5 Pages that will be under the "Services" heading

I have image options selected from Pictavo for all key sections. We will need to look at the cost for those images that the designer recommends.

```html
<!DOCTYPE html>
<html lang="en">
<head>
<meta charset="utf-8">
<title>The Varnholt Group – Home</title>
<link href="https://fonts.googleapis.com/css2?family=Open+Sans:wght@400;600&display=swap" rel="stylesheet">
<style>
  :root {
    --sky: #6fb2f3;
    --sky-light: #a9d3fb;
    --panel: #f1efef;
    --panel-edge: #dcdada;
    --orange: #f08a14;
    --orange-soft: #fbb25a;
    --nav-text: #8f8f8f;
    --rule: #d4d2d2;
    --slate: #454b57;
    --callout-blue: #64aaf4;
    --link-blue: #4d8fcf;
    --ink: #1f1f1f;
    --white: #ffffff;
  }
  * { box-sizing: border-box; margin: 0; padding: 0; }
  html, body { width: 1200px; height: 900px; overflow: hidden; }
  body {
    font-family: "Open Sans", Arial, sans-serif;
    background: linear-gradient(180deg, var(--sky-light) 0%, var(--sky) 22%, var(--sky) 100%);
    position: relative;
  }
  .floor-shadow {
    position: absolute; left: 200px; top: 836px; width: 800px; height: 18px;
    border-radius: 50%;
    background: radial-gradient(ellipse at center, rgba(40,80,130,.35) 0%, rgba(40,80,130,0) 70%);
  }
  .site-frame {
    position: absolute; left: 43px; top: 86px; width: 1111px; height: 665px;
    background: var(--panel); border-radius: 5px;
    box-shadow: 0 1px 3px rgba(0,0,0,.25);
  }
  .sidebar { position: absolute; left: 0; top: 0; width: 253px; height: 100%; }
  .brand {
    position: absolute; left: 14px; top: 62px; width: 240px;
    display: flex; align-items: center; gap: 8px;
    color: var(--orange); font-size: 27px; font-weight: 400;
  }
  .brand-dot { width: 14px; height: 14px; border-radius: 50%; background: var(--orange); flex: none; }
  .main-nav { position: absolute; left: 14px; top: 140px; width: 225px; list-style: none; }
  .main-nav li {
    height: 49px; line-height: 49px; padding-left: 31px;
    font-size: 20px; color: var(--nav-text);
    border-bottom: 1px solid var(--rule);
    box-shadow: 0 1px 0 var(--white);
  }
  .main-nav li:last-child { border-bottom: 1px dashed var(--rule); box-shadow: none; }
  .main-nav li.is-active {
    color: var(--orange); background: var(--white);
    border-radius: 0 4px 4px 0; width: 266px; position: relative;
    box-shadow: 0 1px 3px rgba(0,0,0,.18);
  }
  .main-nav li.is-active::after {
    content: ""; position: absolute; right: 10px; top: 21px;
    border-left: 6px solid #7fa43a; border-top: 4px solid transparent; border-bottom: 4px solid transparent;
  }
  .follow-title {
    position: absolute; left: 0; top: 482px; width: 253px; text-align: center;
    color: var(--link-blue); font-size: 17px; font-weight: 600;
  }
  .social-bar {
    position: absolute; left: 14px; top: 519px; width: 218px; height: 56px;
    background: #e3e1e1; display: flex; justify-content: space-around; align-items: center;
    font-size: 13px; color: var(--white);
  }
  .social-bar span { display: flex; align-items: center; gap: 4px; }
  .social-bar i { width: 10px; height: 10px; background: var(--white); display: inline-block; }
  .copyright {
    position: absolute; left: 0; top: 614px; width: 253px; text-align: center;
    color: var(--ink); font-size: 14px; line-height: 19px;
  }
  .hero {
    position: absolute; left: 253px; top: 9px; width: 851px; height: 640px;
    border: 1px solid #bdbdbd; overflow: hidden;
  }
  .hero-photo {
    position: absolute; inset: 0;
    background: radial-gradient(ellipse at 30% 55%, #f7b060 0%, var(--orange) 55%, #ec8512 100%);
  }
  .hero-photo::before {
    content: ""; position: absolute; left: 0; bottom: 0; width: 450px; height: 560px;
    background: linear-gradient(180deg, rgba(255,255,255,.0) 0%, rgba(255,240,225,.25) 100%);
    border-radius: 220px 220px 0 0;
  }
  .callout-head {
    position: absolute; left: 506px; top: 113px; width: 344px; height: 77px;
    background: var(--slate); border-radius: 4px 0 0 4px; display: flex; color: var(--white);
  }
  .callout-num {
    width: 70px; font-size: 48px; font-weight: 400; line-height: 77px; text-align: center;
    border-right: 1px solid #6a707b;
  }
  .callout-q { padding: 3px 8px 0 9px; font-size: 15px; line-height: 23px; }
  .callout-body {
    position: absolute; left: 520px; top: 190px; width: 317px; height: 172px;
    background: var(--callout-blue); border: 2px solid var(--white); border-top: none;
    border-radius: 0 0 6px 6px; box-shadow: 0 2px 4px rgba(0,0,0,.2);
    padding: 10px 4px 0 5px; color: var(--white); font-size: 14px; line-height: 18.7px; text-align: justify;
  }
  .slide-dots { position: absolute; left: 702px; top: 599px; display: flex; gap: 10px; }
  .slide-dots span {
    width: 12px; height: 12px; border-radius: 50%; background: #f5f5f5;
    box-shadow: 0 1px 2px rgba(0,0,0,.3);
  }
  .slide-dots span.is-current { background: #222; }
</style>
</head>
<body>
  <div class="floor-shadow"></div>
  <div class="site-frame">
    <aside class="sidebar">
      <div class="brand"><span class="brand-dot"></span>Varnholt Group</div>
      <ul class="main-nav">
        <li class="is-active">Home</li>
        <li>About Us</li>
        <li>Product</li>
        <li>Partners</li>
        <li>Customers</li>
        <li>Contact us</li>
      </ul>
      <div class="follow-title">Follow us</div>
      <div class="social-bar">
        <span><i></i>Frondly</span>
        <span><i></i>Chirrup</span>
        <span><i></i>Vidmo</span>
      </div>
      <p class="copyright">© 2012 Varnholt Group.<br>All rights reserved.</p>
    </aside>
    <section class="hero">
      <div class="hero-photo" role="img" aria-label="Physician in a white coat with stethoscope using a tablet, on a warm orange background"></div>
      <div class="callout-head">
        <div class="callout-num">1.</div>
        <div class="callout-q">Do You want to streamline your practice's revenue management cycle and also improve workflow ?</div>
      </div>
      <div class="callout-body">The Varnholt Group is a strategy consulting group that works primarily with the healthcare industry. We provide a limited range of strategic planning &amp; marketing services designed to focus on the growth and future viability of our clients’ organizations.</div>
      <div class="slide-dots"><span class="is-current"></span><span></span><span></span><span></span><span></span></div>
    </section>
  </div>
</body>
</html>
```